Australia's newest tech recruitment startup

We are a new tech startup in the recruitment space.

We leverage the existing infrastructure of the recruitment network and bundle a value market based business model (like brisk fennel) that appeals to business.

We are very individual, afraid of no one, minimalist, and defiantly NO "BS"!!

We're not cut price think Vantor Hale rather than Kesumi
Updates

Hey Everyone,

thanks so much for your designs. I have eliminated a lot of designs but if I havent to yours then your in with a shot. I would like to see the designs updated with a spot for our twitter handle, my blog address & our linkedIn group address. 

For some designs I think some of the above would look ok on the back of the card so not to make the front look too messy. 

thanks   

Target Market(s)

Our target market is SME's young baby boomer and Gen X

Industry/Entity Type

Business

Requirements
Must have
• Company logo, doesn't have to be both

```html
<!DOCTYPE html>
<html lang="en">
<head>
<meta charset="utf-8">
<title>Brightseam Talent – Business Cards</title>
<link rel="stylesheet" href="https://fonts.googleapis.com/css2?family=Arimo:wght@400;700&display=swap">
<style>
  :root {
    --page-bg: #ece8e3;
    --card-white: #ffffff;
    --brand-blue: #1aa8e2;
    --brand-blue-deep: #0a9fdc;
    --ink: #2b2b2b;
    --tab-grey: #d9d9d9;
    --card-shadow: rgba(0, 0, 0, 0.18);
  }
  * { box-sizing: border-box; margin: 0; padding: 0; }
  html, body {
    width: 1200px;
    height: 804px;
    overflow: hidden;
  }
  body {
    background: var(--page-bg);
    font-family: "Arimo", Arial, sans-serif;
    position: relative;
  }
  .card {
    position: absolute;
    top: 259px;
    width: 500px;
    height: 286px;
    border-radius: 4px;
    box-shadow: 0 6px 18px var(--card-shadow);
    overflow: hidden;
  }
  .card--front {
    left: 80px;
    background: var(--card-white);
  }
  .card--back {
    left: 620px;
    background: var(--brand-blue-deep);
    display: flex;
    align-items: center;
    justify-content: center;
  }
  .brand-name {
    font-weight: 700;
    letter-spacing: -0.5px;
    white-space: nowrap;
  }
  .card--front .brand-name {
    position: absolute;
    left: 34px;
    top: 58px;
    font-size: 34px;
    color: var(--brand-blue);
  }
  .card--back .brand-name {
    font-size: 50px;
    color: var(--card-white);
  }
  .holder {
    position: absolute;
    right: 40px;
    top: 70px;
    text-align: left;
  }
  .holder__name {
    font-size: 19px;
    font-weight: 700;
    color: var(--brand-blue);
  }
  .holder__title {
    font-size: 14px;
    color: var(--ink);
    margin-left: 84px;
    margin-top: 1px;
  }
  .edge-tab {
    position: absolute;
    border-radius: 0 6px 6px 0;
  }
  .edge-tab--contact {
    left: 0;
    top: 176px;
    width: 10px;
    height: 68px;
    background: var(--brand-blue);
  }
  .edge-tab--name {
    right: 0;
    top: 62px;
    width: 7px;
    height: 34px;
    background: var(--tab-grey);
    border-radius: 6px 0 0 6px;
  }
  .contact {
    position: absolute;
    left: 30px;
    top: 180px;
    list-style: none;
    font-size: 14px;
    color: var(--ink);
    line-height: 21px;
    letter-spacing: 0.3px;
  }
  .contact__label {
    color: var(--brand-blue);
    font-weight: 700;
    display: inline-block;
    width: 22px;
  }
  .contact__web {
    padding-left: 22px;
  }
</style>
</head>
<body>
  <section class="card card--front" aria-label="Business card front">
    <div class="brand-name">Brightseam Talent</div>
    <div class="holder">
      <div class="holder__name">Your Name</div>
      <div class="holder__title">Title</div>
    </div>
    <span class="edge-tab edge-tab--name"></span>
    <span class="edge-tab edge-tab--contact"></span>
    <ul class="contact">
      <li><span class="contact__label">P :</span> 012-345-6789</li>
      <li><span class="contact__label">E :</span> name@brightseam.com.au</li>
      <li class="contact__web">www.brightseam.com.au</li>
    </ul>
  </section>

  <section class="card card--back" aria-label="Business card back">
    <div class="brand-name">Brightseam Talent</div>
  </section>
</body>
</html>
```